Harbor Lane Consignment Brochure

We need a brochure to showcase our consignment business. We are a company that sells event tickets (sports, concerts, theatre, etc...) on the secondary market. We are now starting a new business venture where other companies like ours can sell through us, leveraging our technology, and our infrastructure to grow their business.

We want to showcase the benefits of consigning with us, instead of doing things on your own. By using our services companies won't have to deal with providing customer support, packaging and delivering tickets, fighting credit card charge-backs. They also won't need to pay for expensive software utilities, point-of-sale licenses, and exchange fees. (An exchange is where they list tickets, like SeatKiosk.com or PassVault.com).
Updates

We've decided we have to scrap the testimonials page, so instead of testimonials, let's go with this: OUR PROMISE TO YOU: The best automation software in the industry. Incredibly fast and accurate pricing. Exposure on every major and minor exchange. Real time sales data on your desktop or phone. Earlier sales for more money. Constantly updated technology and outstanding support. Top-notch staff handling all customer service. On-time packaging and delivery. All while meeting or beating your current exchange rates!

Target Market(s)

We want to advertise that by using our services we'll meet or beat their current rates on the various exchanges (SeatKiosk, AdmitGrid, PassVault, etc...) and save them money by eliminating their need for expensive software and extra labor.
We want to target 2 key demographics.

The first is smaller brokers that do maybe $300k-$500k in annual sales. For these brokers the monthly and yearly expenses of automation software, point-of-sale systems, and website hosting can eat into a large part of their profit. A small time broker could save over $15,000 / year in those expenses alone.

The second target is larger brokers that do several million in annual sales. For these brokers, they're paying for labor to package and deliver tickets (shipping and handling), answer phones and resolve issues (customer support), fight credit card charge-backs. They're also paying for the infrastructure of supporting an office: rent, utilities, etc... A large broker like this could save hundreds of thousands of dollars by reducing their need for all that labor, which would in turn reduce their need for a large office space

Industry/Entity Type

Credit Card

Requirements
Must have
• Tri-fold layout
Use the logo provided (if you need .AI or .PSD version of it I can provide them)
Color-schema that fits well with the logo
Website URL: www.harborlaneconsignment.example
Contact Email: contact@harborlaneconsignment.example
Nice to have
• I would like the a page focused on the smaller brokers and another page focused on the larger brokers (based on the information provided previously)

```html
<!DOCTYPE html>
<html lang="en">
<head>
<meta charset="utf-8">
<title>Harbor Lane Consignment – Tri-fold Brochure Inside</title>
<link rel="stylesheet" href="https://fonts.googleapis.com/css2?family=Arimo:wght@400;700&family=Montserrat:wght@600;700;800&display=swap">
<style>
  :root {
    --navy: #26349a;
    --green: #2bb04a;
    --stone: #e3e1da;
    --ink: #2a2a2a;
    --paper: #ffffff;
  }
  * { box-sizing: border-box; margin: 0; padding: 0; }
  html, body { width: 1200px; height: 933px; overflow: hidden; background: #ffffff; }
  body { font-family: "Arimo", Arial, sans-serif; color: var(--ink); }

  .brochure {
    position: absolute; left: 33px; top: 24px; width: 1140px; height: 862px;
    background: var(--paper);
    box-shadow: 6px 8px 14px rgba(0,0,0,.25);
    overflow: hidden;
  }
  .backdrop, .photo { position: absolute; }
  .backdrop { inset: 0; }

  .panel {
    position: absolute;
    background: rgba(255,255,255,.93);
    -webkit-mask:
      radial-gradient(circle at 50% 0, transparent 23px, #000 24px) top / 100% 51% no-repeat,
      radial-gradient(circle at 50% 100%, transparent 23px, #000 24px) bottom / 100% 51% no-repeat;
    mask:
      radial-gradient(circle at 50% 0, transparent 23px, #000 24px) top / 100% 51% no-repeat,
      radial-gradient(circle at 50% 100%, transparent 23px, #000 24px) bottom / 100% 51% no-repeat;
    text-align: center;
    font-size: 11px;
    line-height: 1.4;
  }
  .panel-about    { left: 18px;  top: 96px; width: 322px; height: 620px; padding: 66px 20px 0; }
  .panel-tech     { left: 396px; top: 99px; width: 330px; height: 608px; padding: 82px 22px 0; }
  .panel-overhead { left: 771px; top: 92px; width: 323px; height: 644px; padding: 64px 20px 0; }

  .pill {
    display: inline-block; background: var(--green); color: #fff;
    font-family: "Montserrat", Arial, sans-serif; font-weight: 700; font-size: 15.5px;
    padding: 6px 15px; border-radius: 12px; letter-spacing: .3px;
  }
  .panel-about p { margin: 12px 0 0; }
  .section + .section { margin-top: 22px; }

  .headline {
    background: var(--navy); color: #fff; border-radius: 12px;
    font-family: "Montserrat", Arial, sans-serif; font-weight: 700;
    padding: 7px 8px; line-height: 1.2; white-space: nowrap;
  }
  .headline .kicker { display: block; font-size: 13px; }
  .headline .big { display: block; font-size: 18px; letter-spacing: .3px; }
  .panel-tech .headline { margin: 0 12px; }
  .panel-overhead .headline { margin: 0 6px; }
  .panel-overhead .headline .kicker { font-size: 13.5px; }
  .panel-overhead .headline .big { font-size: 19px; }

  .lede { margin-top: 14px; }

  .cost-list {
    list-style: none; background: var(--green); color: #fff; border-radius: 14px;
    font-family: "Montserrat", Arial, sans-serif; font-weight: 700; font-size: 12.5px;
    line-height: 1.3; padding: 14px 10px;
  }
  .cost-list li + li { margin-top: 16px; }
  .panel-tech .cost-list { margin: 16px -6px 0; }
  .panel-overhead .cost-list { margin: 24px 0 0; padding: 16px 10px; }
  .panel-overhead .cost-list li + li { margin-top: 14px; }

  .grand-total {
    font-family: "Montserrat", Arial, sans-serif; font-weight: 700; font-size: 14.5px;
    color: var(--green); margin-top: 22px; letter-spacing: .2px; white-space: nowrap;
  }
  .grand-total span { color: var(--navy); }
  .panel-overhead .grand-total { margin-top: 30px; }
  .closing { margin-top: 20px; padding: 0 12px; }
  .panel-overhead .closing { margin-top: 40px; padding: 0 16px; }

  .brand {
    position: absolute; left: 444px; top: 733px; width: 230px; height: 96px;
    background: #fff; border-radius: 12px;
    box-shadow: 2px 4px 8px rgba(0,0,0,.3);
    display: flex; align-items: center; justify-content: center; gap: 8px;
    font-family: "Montserrat", Arial, sans-serif; font-weight: 800; color: var(--navy);
    font-size: 17px; line-height: 1.1; text-align: left;
  }
  .brand-dot { width: 22px; height: 22px; border-radius: 50%; background: var(--green); flex: none; }
</style>
</head>
<body>
<main class="brochure">
  <svg class="backdrop" width="1140" height="862" viewBox="0 0 1140 862" aria-hidden="true">
    <rect x="0" y="49" width="1140" height="813" fill="var(--stone)"/>
    <rect x="0" y="0" width="1140" height="49" fill="var(--navy)"/>
    <path d="M0 640 Q570 520 1140 640 L1140 812 L0 812 Z" fill="var(--navy)"/>
    <ellipse cx="570" cy="400" rx="690" ry="330" fill="#ffffff"/>
    <path d="M0 700 Q300 760 570 762 Q840 760 1140 700 L1140 812 L0 812 Z" fill="var(--navy)"/>
    <rect x="0" y="812" width="1140" height="8" fill="#ffffff"/>
    <rect x="0" y="820" width="1140" height="16" fill="var(--stone)"/>
    <rect x="0" y="836" width="1140" height="26" fill="#ffffff"/>
  </svg>
  <svg class="photo" style="left:160px;top:78px" width="820" height="680" viewBox="0 0 820 680" role="img" aria-label="Blurred photo of a printed event ticket held in hand">
    <defs>
      <radialGradient id="photoTone" cx="45%" cy="40%" r="65%">
        <stop offset="0" stop-color="#eef0f4"/>
        <stop offset=".45" stop-color="#c7ccd6"/>
        <stop offset=".75" stop-color="#a39a95"/>
        <stop offset="1" stop-color="#8c95a8"/>
      </radialGradient>
    </defs>
    <ellipse cx="410" cy="340" rx="405" ry="335" fill="url(#photoTone)"/>
  </svg>

  <section class="panel panel-about">
    <div class="section">
      <h2 class="pill">WHO WE ARE</h2>
      <p>We are an industry-leading ticket broker in business for almost 30 years. We're now offering our efficiency and expertise to select members of the broker community as a consignment service.</p>
    </div>
    <div class="section">
      <h2 class="pill">WHAT WE DO</h2>
      <p>We sell tickets. Lots of them! Using a combination of industry standard and proprietary software and an amazing staff we handle all of the receiving, downloading, scanning, packaging, shipping, uploading, and customer service, so you can do <strong>what you do best:</strong> buy and sell more tickets!</p>
    </div>
    <div class="section">
      <h2 class="pill">HOW IT WORKS</h2>
      <p>Using our web-based portal you can access our system from anywhere in the world to buy-in and price your inventory. We list your tickets on every major ticket exchange at a rate that matches or beats your current rate. When your tickets arrive you send them in bulk to our offices and we handle the rest. You receive payment twice a month for all tickets that have been sold and delivered.</p>
    </div>
  </section>

  <section class="panel panel-tech">
    <h2 class="headline"><span class="kicker">LEVERAGE OUR TECHNOLOGY</span><span class="big">SAVE THOUSANDS!</span></h2>
    <p class="lede">To compete in today's market you need every technological advantage possible. You could spend thousands every year on expensive automation software, point of sale systems, web hosting, server hosting, point-of-sale systems, and exchange fees – or you could consign with us and enjoy all those benefits without the hefty price tag.</p>
    <ul class="cost-list">
      <li>Point-of-Sale System: $2400/year</li>
      <li>Exchange Fees: $5700/year</li>
      <li>Website / Server Infrastructure: $3000/year</li>
      <li>Automation Software: $4500/year</li>
    </ul>
    <p class="grand-total">GRAND TOTAL: <span>OVER $15,000/YEAR!</span></p>
    <p class="closing">That's money you could spend on growing your business or better enjoying all the free time you'll have while we take care of the day-to-day operations.</p>
  </section>

  <section class="panel panel-overhead">
    <h2 class="headline"><span class="kicker">LOWER YOUR OVERHEAD</span><span class="big">GROW YOUR BUSINESS!</span></h2>
    <p class="lede">A large broker has a lot of overhead. You need people to assist customers, deal with exchanges, package and ship orders, combat fraud, fight credit card charge-backs, and constantly monitor your inventory to ensure no mistakes are being made. What if you didn't need to worry about all of that extra labor and the overhead associated with it?</p>
    <ul class="cost-list">
      <li>Customer Support &amp; Sales Labor: $45,000/person/year</li>
      <li>Large Office Lease: $40,000/year</li>
      <li>IT Support / Infrastructure: $30,000/</li>
    </ul>
    <p class="grand-total">GRAND TOTAL: <span>100'S OF THOUSANDS</span></p>
    <p class="closing">Eliminate the overhead and headache that comes with running a large brokerage. Use Harbor Lane Consignment to handle it for you.</p>
  </section>

  <div class="brand">
    <span class="brand-dot"></span>
    <span>HARBOR LANE<br>CONSIGNMENT</span>
  </div>
</main>
</body>
</html>
```